ALL TEXT Social Media Graphics

We are looking for a series of social media graphics for Instagram (new size: 4:5 (1080 x 1350 pixels) ratio that are ALL TEXT. We want the following quotes below on each graphic; one quote per graphic. AND, In very small letters at the bottom of each graphic, add @PaulaWrenLive
The look and feel of these graphics should be complimentary to the color palette attached below; but keep them simple. But the design is up to you; at the end of this document, I provided various samples of all text graphics that I like as examples.
The Quotes are in the attached WORD document
women trying to lose weight

```html
<!DOCTYPE html>
<html lang="en">
<head>
<meta charset="utf-8">
<title>Glow Girl Summer Shapeup – Social Graphics</title>
<link rel="stylesheet" href="https://fonts.googleapis.com/css2?family=Anton&family=Arimo:ital,wght@0,400;0,700;1,700&display=swap">
<style>
  :root {
    --backdrop: #a3a3a3;
    --card: #ffffff;
    --pink: #ec4783;
    --plum: #6b1f56;
    --ink: #222222;
    --muted: #555555;
  }
  * { box-sizing: border-box; margin: 0; padding: 0; }
  html, body { width: 1200px; height: 2892px; overflow: hidden; }
  body {
    background: var(--backdrop);
    font-family: "Arimo", Arial, sans-serif;
  }
  .grid {
    display: grid;
    grid-template-columns: repeat(2, 536px);
    grid-auto-rows: 540px;
    column-gap: 24px;
    row-gap: 27px;
    padding: 28px 0 0 52px;
  }
  .post {
    background: var(--card);
    padding: 44px 48px 28px;
    display: flex;
    flex-direction: column;
    position: relative;
    overflow: hidden;
  }
  .headline {
    font-family: "Anton", "Arial Narrow", sans-serif;
    font-weight: 400;
    font-size: 48px;
    line-height: 1.1;
    color: var(--pink);
    margin-bottom: 22px;
  }
  .headline.plum { color: var(--plum); }
  .hl-plum { color: var(--plum); }
  .hl-pink { color: var(--pink); }
  .lead {
    font-weight: 700;
    font-style: italic;
    font-size: 22px;
    line-height: 1.3;
    color: var(--ink);
    margin-bottom: 20px;
  }
  .cta {
    font-size: 24px;
    line-height: 1.3;
    color: var(--plum);
  }
  .cta strong { font-weight: 700; }
  .handle {
    position: absolute;
    left: 48px;
    bottom: 26px;
    font-size: 13px;
    color: var(--muted);
  }
</style>
</head>
<body>
<main class="grid">

  <article class="post">
    <h2 class="headline">You can absolutely be down 20–30 POUNDS by end of summer.</h2>
    <p class="lead">All it takes is the right plan—and you’ve found it.</p>
    <p class="cta">Comment “<strong>GLOW GIRL</strong>” for the Glow Girl Summer Shapeup!</p>
    <span class="handle">@PaulaWrenLive</span>
  </article>

  <article class="post">
    <h2 class="headline plum">YOU DON’T NEED another diet—you need a system that works.</h2>
    <p class="lead">Drop <span class="hl-pink">30 pounds</span> with the Glow Girl Summer Shapeup.</p>
    <p class="cta">Comment “<strong>Summer</strong>” to start now.</p>
    <span class="handle">@PaulaWrenLive</span>
  </article>

  <article class="post">
    <h2 class="headline">This summer ain’t over—and neither are <span class="hl-plum">YOUR BODY GOALS.</span></h2>
    <p class="lead">Drop <span class="hl-pink">30 pounds</span> with the Glow Girl Summer Shapeup.</p>
    <p class="cta">Comment “<strong>Glow Girl</strong>” to get the plan.</p>
    <span class="handle">@PaulaWrenLive</span>
  </article>

  <article class="post">
    <h2 class="headline plum">If your goal is a tiny waist, flat belly, and <span class="hl-pink">30 POUNDS</span> down—this is the plan.</h2>
    <p class="cta">Comment “<strong>Summer</strong>” to join the Glow Girl Summer Shapeup!</p>
    <span class="handle">@PaulaWrenLive</span>
  </article>

  <article class="post">
    <h2 class="headline">There’s still time to drop the <span class="hl-plum">30 POUNDS</span> and slay this summer.</h2>
    <p class="lead">The <span class="hl-pink">Glow Girl Summer</span> Shapeup has the blueprint.</p>
    <p class="cta">Comment “<strong>Glow Girl</strong>”!</p>
    <span class="handle">@PaulaWrenLive</span>
  </article>

  <article class="post">
    <h2 class="headline">Snatched waist, flat tummy, <span class="hl-plum">30 POUNDS</span> lighter</h2>
    <p class="lead">—that’s what <span class="hl-pink">Glow Girl Summer</span> Shapeup Challenge delivers.</p>
    <p class="cta">Comment “<strong>Glow Girl</strong>” to get the plan</p>
    <span class="handle">@PaulaWrenLive</span>
  </article>

  <article class="post">
    <h2 class="headline">Nothing feels better than seeing that <span class="hl-plum">SCALE DROP WEEK AFTER WEEK.</span></h2>
    <p class="lead">Let’s lose up to <span class="hl-pink">30 pounds</span> this summer—together.</p>
    <p class="cta">Comment “<strong>Summer</strong>” to join the Glow Girl Summer Shapeup!</p>
    <span class="handle">@PaulaWrenLive</span>
  </article>

  <article class="post">
    <h2 class="headline">Sis, we’re dropping <span class="hl-plum">BELLY FLAT</span> and saying goodbye to <span class="hl-plum">STUBBORN POUNDS.</span></h2>
    <p class="cta">Join the <strong>Glow Girl Summer</strong> Shapeup—comment “<strong>Summer</strong>”!</p>
    <span class="handle">@PaulaWrenLive</span>
  </article>

  <article class="post">
    <h2 class="headline">Don’t wait ’til next summer to get right. <span class="hl-plum">THE TIME IS NOW.</span></h2>
    <p class="lead">Drop <span class="hl-pink">30 pounds</span> with the Glow Girl Summer Shapeup.</p>
    <p class="cta">Comment “<strong>Summer</strong>”</p>
    <span class="handle">@PaulaWrenLive</span>
  </article>

  <article class="post">
    <h2 class="headline">You’ve got 8 weeks and the perfect plan to drop <span class="hl-plum">30 POUNDS.</span></h2>
    <p class="lead">Let’s get snatched this summer with the <span class="hl-pink">Glow Girl Summer Shapeup.</span></p>
    <p class="cta">Comment “<strong>Summer</strong>”</p>
    <span class="handle">@PaulaWrenLive</span>
  </article>

</main>
</body>
</html>
```